Brindle Tavern & Lodge Supplies need a website

We need a website designed and created to facilitate us to promote & sell our products online. We buy excess / clearance lots of pub, cafe, restaurant & hotel furniture and equipment (usually from businesses that have excess inventory after a refurb or have closed down). We then sell these to other businesses mainly through our Chatterly page "Brindle Tavern & Lodge Supplies" but the process is cumbersome for the following reasons:
1) We dont have a stock list and images as it changes daily and people can only rely on recent posts and dont know if something is for sale still or is sold
2) we do not have the facility to sell online.

We are open to ideas and design concepts

We already have a logo & stationery deisgned

its probably best to look through our Chatterly page to better understand what we do

We would consider a catalogue / by department / category user interface such as:
https://brambleworth-trade-fittings.co.uk/

Our preference would be to change / delete / update stock via smartphone to best facilitate the maintenance of the website which i will do myself

Suggested categories would include:
Bar Furniture
Bar Equipment
Restaurant Furniture
Catering Equipment
Bedroom Furniture
Miscellaneous

Sub categories would include:
Bar Furniture:
Bar Stools
Bar Tables
Benches
Tub chairs
Arm chairs
Pub Mirrors
Pub Signs
Pub Memorabilia

Bar Equipment:
Bottle Coolers
Ice Machines
Glass Washers
Tills
Lighting
Sound
Wireless waiter
Glassware
Taps
Line coolers
Snooker tables
Pool tables
gaming machines

Restaurant Furniture:
Tables
Chairs
Wine racks
Dressers
Couches
Bench seating
Tub Chairs
Arm chairs
High chairs
Menu boards
Mirrors
Pictures

Catering Equipment:
Fridges
Freezers
Ovens
Cookers
Fryers
Carvery units
Hot display units
Refrigerated displays
Sinks
Stainless steel units
Microwaves
Mixers
Crockery
Cutlery
Utensils
Glassware

Bedroom Furniture:
Beds
Headboards
Wardrobes
Lockers
Dressing Tables
Mirrors
Lamps
Pictures

Profit sharing schemes:
Pool Tables
Juke Boxes
Gaming Machines

Target Market(s)

Pubs
Restaurants
cafes
guest houses
hotels

Industry/Entity Type

Hospitality

Number of Pages Required

5+ page

Colors

Designer to choose colors to be used in the design.

Requirements
Must have
• Website featuring our categories of stock to sell
Nice to have
• Ecommerce option
Should not have
• just a front page

```html
<!DOCTYPE html>
<html lang="en">
<head>
<meta charset="utf-8">
<title>Brindle Tavern &amp; Lodge Supplies</title>
<link href="https://fonts.googleapis.com/css2?family=Raleway:wght@300;400;500;600;700;800&display=swap" rel="stylesheet">
<style>
:root{
  --red:#b3131d;
  --red-dark:#8f0e16;
  --ink:#262626;
  --ink-2:#1e1e1e;
  --text:#555;
  --muted:#8a8a8a;
  --line:#dcdcdc;
  --paper:#ffffff;
  --soft:#efefef;
}
*{box-sizing:border-box;margin:0;padding:0}
html,body{width:1200px;height:3488px;overflow:hidden}
body{font-family:'Raleway',sans-serif;color:var(--text);background:var(--paper);position:relative}
.abs{position:absolute}
.btn{position:absolute;background:var(--red);color:#fff;font-size:15px;display:flex;align-items:center;justify-content:center;letter-spacing:.5px}

/* hero */
.hero{left:0;top:0;width:1200px;height:612px;background:linear-gradient(180deg,#e9e6e2 0%,#d9d4ce 50%,#c8c2bb 100%)}
.hero-photo{left:0;top:0;width:1200px;height:612px;background:radial-gradient(ellipse at 75% 30%,#a9b58f 0%,rgba(169,181,143,0) 45%),radial-gradient(ellipse at 40% 75%,#f4f2ef 0%,rgba(244,242,239,0) 50%);opacity:.8}
.contact-line{left:86px;font-size:14px;color:#333;display:flex;align-items:center;gap:10px}
.menu-icon{left:1088px;top:36px;width:26px}
.menu-icon span{display:block;height:3px;background:#333;margin-bottom:5px}
.brand{left:0;width:1200px;top:120px;text-align:center}
.brand-mark{width:54px;height:54px;background:var(--red);margin:0 auto 14px}
.brand-name{font-weight:800;font-size:24px;color:#1a1a1a;letter-spacing:.5px;text-transform:uppercase;white-space:nowrap}
.brand-rule{width:440px;height:2px;background:#1a1a1a;margin:10px auto 0}
.hero-title{left:0;width:1200px;top:296px;text-align:center;color:var(--red);font-weight:800;font-size:40px;line-height:56px;text-transform:uppercase;letter-spacing:.5px}
.hero-btn{left:481px;top:449px;width:238px;height:40px;font-weight:800;letter-spacing:2px;font-size:15px}

/* seller / buyer */
.trade{left:0;top:612px;width:1200px;height:270px;background:var(--ink)}
.trade-col h3{font-size:21px;color:#fff;font-weight:500;text-transform:uppercase;letter-spacing:.5px}
.trade-col p{font-size:14px;line-height:21px;color:#ccc;margin-top:14px;width:320px}
.divider-v{left:601px;top:664px;width:2px;height:160px;background:#777}

/* section headings */
.section-title{left:0;width:1200px;text-align:center;font-size:32px;font-weight:400;color:#333;letter-spacing:1px;text-transform:uppercase}

/* categories */
.tabs{left:95px;top:1000px;width:1010px;height:47px;display:flex;box-shadow:0 2px 6px rgba(0,0,0,.18);background:#fff}
.tab{flex:1 1 auto;display:flex;align-items:center;justify-content:center;font-size:13px;color:#444;text-transform:uppercase;border-right:1px solid var(--line);padding:0 14px}
.tab.active{background:var(--red);color:#fff;position:relative}
.tab.active::after{content:"";position:absolute;left:50%;bottom:-14px;margin-left:-14px;border-left:14px solid transparent;border-right:14px solid transparent;border-top:14px solid var(--red)}
.feature{left:86px;top:1103px;width:324px;height:369px;background:linear-gradient(160deg,#6e4a2e,#3d2a1f 55%,#7a5b3d)}
.feature-label{left:86px;top:1408px;width:324px;height:64px;background:var(--red);color:#fff;font-size:21px;text-transform:uppercase;display:flex;align-items:center;justify-content:center}
.tile{position:absolute;width:149px;height:167px;background:#fff;box-shadow:0 1px 4px rgba(0,0,0,.2)}
.tile .ph{width:149px;height:125px}
.tile .lbl{height:42px;display:flex;align-items:center;justify-content:center;font-size:13px;color:#666;text-transform:uppercase}

/* offer */
.offer-band{left:0;top:1535px;width:1200px;height:524px;background:linear-gradient(180deg,#8b8582,#6d6765 50%,#8d7f7c)}
.offer-panel{left:86px;top:1640px;width:1028px;height:318px;background:rgba(255,255,255,.88)}
.offer-title{left:110px;top:1660px;width:560px;font-size:31px;font-weight:800;color:#111;text-transform:uppercase;line-height:40px}
.offer-title em{font-style:normal;color:var(--red);font-size:39px}
.offer-text{left:110px;top:1810px;width:560px;font-size:14px;line-height:21px;color:#555}
.offer-photo{left:707px;top:1600px;width:319px;height:396px;border:6px solid #fff;box-shadow:0 4px 12px rgba(0,0,0,.4);background:linear-gradient(170deg,#2b2b2b,#111 60%,#3b3b3b)}

/* testimonial */
.quote-box{left:191px;top:2180px;width:879px;height:167px;border:2px solid var(--red);background:#fff}
.avatar{left:126px;top:2194px;width:134px;height:134px;border-radius:50%;border:4px solid var(--red);background:linear-gradient(180deg,#c9c4bd,#7f8f99)}
.quote-mark{left:230px;top:2192px;width:52px;height:52px;border-radius:50%;background:var(--red)}
.quote-name{left:304px;top:2214px;color:var(--red);font-size:15px;font-style:italic}
.quote-text{left:304px;top:2244px;width:740px;font-size:15px;line-height:23px;color:#444}
.arrow{position:absolute;top:2330px;width:38px;height:38px;border-radius:50%;border:2px solid var(--red);background:#fff;display:flex;align-items:center;justify-content:center}
.arrow.solid{background:var(--red)}

/* blog */
.blog{left:0;top:2431px;width:1200px;height:586px;background:var(--soft)}
.post{position:absolute;top:2554px;width:502px;height:330px;box-shadow:0 3px 8px rgba(0,0,0,.3)}
.post .date{position:absolute;left:0;top:0;width:72px;height:84px;background:var(--red);color:#fff;font-size:12px;font-weight:700;text-align:center;padding-top:50px}
.post .cap{position:absolute;left:0;bottom:0;width:100%;height:108px;background:rgba(0,0,0,.62);padding:16px 24px;color:#fff}
.post .cap h4{font-size:17px;font-weight:700}
.post .cap p{font-size:14px;line-height:20px;color:#ddd;margin-top:8px}

/* newsletter */
.news-band{left:0;top:3017px;width:1200px;height:146px;background:var(--red)}
.news-title{left:86px;top:3055px;font-size:31px;line-height:40px;color:#fff;font-weight:700;letter-spacing:.5px}
.news-input{left:554px;top:3050px;width:426px;height:50px;background:#fff;font-size:14px;color:#999;padding:0 16px;display:flex;align-items:center}
.news-btn{left:980px;top:3050px;width:136px;height:50px;background:var(--ink-2);color:#fff;font-size:14px;font-weight:700;display:flex;align-items:center;justify-content:center}

/* footer */
.footer{left:0;top:3163px;width:1200px;height:325px;background:var(--ink-2)}
.foot-brand{left:86px;top:3196px;width:284px;text-align:center}
.foot-brand .brand-mark{width:40px;height:40px;background:#fff;margin:0 auto 10px}
.foot-brand .brand-name{color:#fff;font-size:14px;letter-spacing:0}
.foot-brand .brand-rule{width:284px;background:#fff;height:1px;margin-top:8px}
.foot-about{left:86px;top:3290px;width:290px;font-size:14px;line-height:23px;color:#ddd}
.foot-about b{color:#fff}
.foot-col h5{color:var(--red);font-size:15px;font-weight:700;margin-bottom:10px}
.foot-col li{list-style:none;font-size:14px;color:#ddd;line-height:30px}
.addr{display:flex;gap:14px;font-size:14px;color:#ddd;line-height:20px;margin-bottom:14px}
.addr svg{flex:0 0 14px;margin-top:3px}
.social{display:flex;gap:8px;margin-top:10px}
.social span{width:24px;height:24px;background:#1b7fd1}
.foot-rule{left:86px;top:3426px;width:1030px;height:1px;background:#444}
.copy{left:86px;top:3450px;font-size:14px;color:#ccc}
.pay{top:3446px;display:flex;gap:6px;left:952px}
.pay span{width:36px;height:24px;background:#e6e6e6;border-radius:2px}
</style>
</head>
<body>

<!-- hero -->
<header class="abs hero">
  <div class="abs hero-photo" role="img" aria-label="Bright hotel lounge with white chairs, table and greenery by a window"></div>
  <div class="abs contact-line" style="top:22px">
    <svg width="14" height="14" viewBox="0 0 24 24"><path fill="#333" d="M6.6 10.8a15 15 0 0 0 6.6 6.6l2.2-2.2a1 1 0 0 1 1-.25 11 11 0 0 0 3.6.6 1 1 0 0 1 1 1V20a1 1 0 0 1-1 1A17 17 0 0 1 3 4a1 1 0 0 1 1-1h3.5a1 1 0 0 1 1 1 11 11 0 0 0 .6 3.6 1 1 0 0 1-.25 1z"/></svg>
    +353 81 555 0192
  </div>
  <div class="abs contact-line" style="top:44px">
    <svg width="14" height="12" viewBox="0 0 24 20"><path fill="#333" d="M0 2l12 8 12-8V0H0zM0 4v16h24V4l-12 8z"/></svg>
    hello@brindletavernsupplies.ie
  </div>
  <div class="abs menu-icon"><span></span><span></span><span></span></div>
  <div class="abs brand">
    <div class="brand-mark"></div>
    <div class="brand-name">Brindle Tavern &amp; Lodge Supplies</div>
    <div class="brand-rule"></div>
  </div>
  <h1 class="abs hero-title">Buy &amp; Sell Refurb Equipments Lots of<br>Pub, Cafe, Restaurant &amp; Hotel Furniture</h1>
  <div class="btn hero-btn">SHOP NOW</div>
</header>

<!-- seller / buyer -->
<section class="abs trade"></section>
<div class="abs trade-col" style="left:86px;top:664px">
  <h3>We Are Seller</h3>
  <p>The printing and typesetting industry. Lorem Ipsum has been the industry's standard dummy text ever since</p>
</div>
<div class="btn" style="left:86px;top:786px;width:163px;height:36px;font-size:14px">Read More</div>
<svg class="abs" style="left:462px;top:680px" width="122" height="122" viewBox="0 0 122 122">
  <polygon points="61,4 72,18 89,12 92,30 110,33 104,50 118,61 104,72 110,89 92,92 89,110 72,104 61,118 50,104 33,110 30,92 12,89 18,72 4,61 18,50 12,33 30,30 33,12 50,18" fill="none" stroke="#fff" stroke-width="4"/>
  <path d="M42 62h10v24H42zM56 84V62l10-16c3 0 5 3 4 7l-3 8h14c3 0 5 3 4 6l-4 14c-1 2-3 3-5 3z" fill="none" stroke="#fff" stroke-width="4" stroke-linejoin="round"/>
</svg>
<div class="abs divider-v"></div>
<div class="abs trade-col" style="left:614px;top:664px">
  <h3>We Are Buyer</h3>
  <p>The printing and typesetting industry. Lorem Ipsum has been the industry's standard dummy text ever since</p>
</div>
<div class="btn" style="left:614px;top:786px;width:163px;height:36px;font-size:14px">Read More</div>
<svg class="abs" style="left:975px;top:690px" width="144" height="120" viewBox="0 0 144 120">
  <g fill="none" stroke="#fff" stroke-width="5" stroke-linejoin="round" stroke-linecap="round">
    <path d="M4 40l22-22 20 20-22 22zM140 40l-22-22-20 20 22 22z"/>
    <path d="M46 38l18-6c6-2 12 0 16 4l20 18c4 4 0 10-5 7L80 52"/>
    <path d="M30 56l40 40c4 4 10-2 6-6M44 70l30 30c4 4 10-2 6-6M58 84l16 16"/>
    <path d="M100 56L80 76"/>
  </g>
</svg>

<!-- categories -->
<h2 class="abs section-title" style="top:930px">Our Categories</h2>
<nav class="abs tabs">
  <div class="tab active">Bar Furniture</div>
  <div class="tab">Bar Equipment</div>
  <div class="tab">Restaurant Furniture</div>
  <div class="tab">Catering Equipment</div>
  <div class="tab">Bedroom Furniture</div>
  <div class="tab" style="border-right:none">Miscellaneous</div>
</nav>
<div class="abs feature" role="img" aria-label="Warm-lit bar interior with wooden tables and chairs"></div>
<div class="abs feature-label">Bar Furniture</div>

<div class="tile" style="left:437px;top:1103px"><div class="ph" role="img" aria-label="Row of red-topped bar stools" style="background:linear-gradient(180deg,#4a3a34,#2a1f1c)"></div><div class="lbl">Bar Stools</div></div>
<div class="tile" style="left:612px;top:1103px"><div class="ph" role="img" aria-label="Bar tables with black chairs" style="background:linear-gradient(180deg,#6b6058,#2e2a27)"></div><div class="lbl">Bar Tables</div></div>
<div class="tile" style="left:788px;top:1103px"><div class="ph" role="img" aria-label="Upholstered benches" style="background:linear-gradient(180deg,#7c6c5e,#3c332c)"></div><div class="lbl">Benches</div></div>
<div class="tile" style="left:965px;top:1103px"><div class="ph" role="img" aria-label="Leather tub chairs" style="background:linear-gradient(180deg,#6f4f59,#3f5a5a)"></div><div class="lbl">Tub Chairs</div></div>
<div class="tile" style="left:437px;top:1303px"><div class="ph" role="img" aria-label="Dark arm chairs" style="background:linear-gradient(180deg,#555,#222)"></div><div class="lbl">Arm Chairs</div></div>
<div class="tile" style="left:612px;top:1303px"><div class="ph" role="img" aria-label="Decorated pub mirrors" style="background:linear-gradient(180deg,#5b6a6e,#7a3b34)"></div><div class="lbl">Pub Mirrors</div></div>
<div class="tile" style="left:788px;top:1303px"><div class="ph" role="img" aria-label="Stacked pub signs" style="background:linear-gradient(180deg,#6d7174,#3e4347)"></div><div class="lbl">Pub Signs</div></div>
<div class="tile" style="left:965px;top:1303px"><div class="ph" role="img" aria-label="Pub memorabilia on a lit bar" style="background:linear-gradient(180deg,#3c2d22,#1c1511)"></div><div class="lbl">Pub Memorabilia</div></div>

<!-- offer -->
<section class="abs offer-band" role="img" aria-label="Warehouse full of stacked chairs and tables"></section>
<div class="abs offer-panel"></div>
<h2 class="abs offer-title">We Offer <em>Refurb<br>Equipments</em> at Discount<br>Price</h2>
<p class="abs offer-text">Simply Dummy Text Of The Printing And Typesetting Industry. Lorem Ipsum Has Been The Industry's Standard Dummy Text Ever Since Only Five Centuries. imply Dummy Text Of The Printing And Typesetting Industry</p>
<div class="btn" style="left:110px;top:1894px;width:163px;height:36px;font-size:14px">Shop Now</div>
<div class="abs offer-photo" role="img" aria-label="Black bistro table with black chairs"></div>

<!-- testimonial -->
<h2 class="abs section-title" style="top:2110px">Testimonial</h2>
<div class="abs quote-box"></div>
<div class="abs avatar" role="img" aria-label="Customer portrait"></div>
<div class="abs quote-mark">
  <svg width="52" height="52" viewBox="0 0 52 52"><path fill="#fff" d="M15 34v-8c0-5 3-9 8-10v4c-2 1-3 3-3 5h3v9zM28 34v-8c0-5 3-9 8-10v4c-2 1-3 3-3 5h3v9z"/></svg>
</div>
<div class="abs quote-name">— Aidan Kerrigan</div>
<p class="abs quote-text">Lorem Ipsum is simply dummy text of the printing and typesetting industry. Lorem Ipsum has been the industry's standard dummy text ever since the 1500s, when an unknown printer took a galley of type and scrambled it to make a</p>
<div class="arrow" style="left:552px"><svg width="12" height="14" viewBox="0 0 12 14"><path d="M9 1L3 7l6 6" fill="none" stroke="#b3131d" stroke-width="2.5"/></svg></div>
<div class="arrow solid" style="left:598px"><svg width="12" height="14" viewBox="0 0 12 14"><path d="M3 1l6 6-6 6" fill="none" stroke="#fff" stroke-width="2.5"/></svg></div>

<!-- blog -->
<section class="abs blog"></section>
<h2 class="abs section-title" style="top:2482px">Recent Blog Post</h2>
<article class="post" style="left:86px;background:linear-gradient(160deg,#a8855e,#d8c7ae 50%,#b88b48)" role="img" aria-label="Hotel bedroom with bed, dresser and armchair">
  <div class="date"><svg style="position:absolute;left:26px;top:18px" width="20" height="20" viewBox="0 0 20 20"><rect x="2" y="4" width="16" height="14" fill="none" stroke="#fff" stroke-width="2"/><path d="M2 8h16M6 1v5M14 1v5" stroke="#fff" stroke-width="2"/></svg>June 30</div>
  <div class="cap"><h4>Lorem Ipsum is simply dummy text</h4><p>Lorem Ipsum is simply dummy text of the printing and type-setting industry. Lorem Ipsum has beenof type...</p></div>
</article>
<article class="post" style="left:614px;background:linear-gradient(160deg,#3a3a3a,#6e6a64 50%,#2a2a2a)" role="img" aria-label="Outdoor metal chairs around a round table">
  <div class="date"><svg style="position:absolute;left:26px;top:18px" width="20" height="20" viewBox="0 0 20 20"><rect x="2" y="4" width="16" height="14" fill="none" stroke="#fff" stroke-width="2"/><path d="M2 8h16M6 1v5M14 1v5" stroke="#fff" stroke-width="2"/></svg>June 30</div>
  <div class="cap"><h4>Lorem Ipsum is simply dummy text</h4><p>Lorem Ipsum is simply dummy text of the printing and type-setting industry. Lorem Ipsum has beenof type...</p></div>
</article>
<div class="btn" style="left:519px;top:2924px;width:160px;height:34px;font-size:14px">View More</div>

<!-- newsletter -->
<section class="abs news-band"></section>
<h3 class="abs news-title">Subscribe Our Newsletter</h3>
<div class="abs news-input">Enter Email Id</div>
<div class="abs news-btn">Subscribe</div>

<!-- footer -->
<footer class="abs footer"></footer>
<div class="abs foot-brand">
  <div class="brand-mark"></div>
  <div class="brand-name">Brindle Tavern &amp; Lodge Supplies</div>
  <div class="brand-rule"></div>
</div>
<p class="abs foot-about">Simply Dummy Text Of The Printing And Typesetting Industry. Lorem Ipsum Has Been The Industry's Standard Dummy Text Ever Since Only Five Centuries. imply Dummy Text Of The Printing And Typesetting Industry. <b>Read More</b></p>
<div class="abs foot-col" style="left:448px;top:3184px">
  <h5>Quick Links</h5>
  <ul><li>Home</li><li>About Us</li><li>Categories</li><li>Blog</li><li>Testimonial</li><li>Contact Us</li></ul>
</div>
<div class="abs foot-col" style="left:631px;top:3184px">
  <h5>Usefull Links</h5>
  <ul><li>New Products</li><li>Top Sellers</li><li>Manufactrers</li><li>Suppliers</li><li>Specials</li></ul>
</div>
<div class="abs foot-col" style="left:819px;top:3184px;width:300px">
  <h5>Our Address</h5>
  <div class="addr"><svg width="14" height="14" viewBox="0 0 14 14"><path fill="#ddd" d="M7 1L0 7h2v6h4V9h2v4h4V7h2z"/></svg><span>Quarry Lane, Unit 4<br>R14 PX20 Ballyrowan</span></div>
  <div class="addr"><svg width="14" height="14" viewBox="0 0 24 24"><path fill="#ddd" d="M6.6 10.8a15 15 0 0 0 6.6 6.6l2.2-2.2a1 1 0 0 1 1-.25 11 11 0 0 0 3.6.6 1 1 0 0 1 1 1V20a1 1 0 0 1-1 1A17 17 0 0 1 3 4a1 1 0 0 1 1-1h3.5a1 1 0 0 1 1 1 11 11 0 0 0 .6 3.6 1 1 0 0 1-.25 1z"/></svg><span>+353 81 555 0192</span></div>
  <div class="addr"><svg width="14" height="12" viewBox="0 0 24 20"><path fill="#ddd" d="M0 2l12 8 12-8V0H0zM0 4v16h24V4l-12 8z"/></svg><span>hello@brindletavernsupplies.ie</span></div>
  <h5 style="margin-top:8px">Follow Us</h5>
  <div class="social"><span></span><span></span><span></span></div>
</div>
<div class="abs foot-rule"></div>
<div class="abs copy">Copyright © 2018 Brindle Tavern &amp; Lodge Supplies. All Right Reserved.</div>
<div class="abs pay"><span></span><span></span><span></span><span></span></div>

</body>
</html>
```